CD Design Cover - "Beyond the Orchard Gate"

I need a CD cover design. The original Album or CD was recorded in the early eighties. We are re-mastering it. It needs a fresh cover. The genre' is contemporary Christian music and the title of the album is "Beyond the Orchard Gate." This is referring to caring outside of the church walls. A picture of the solo artist could be integrated in the back design. It is not a good picture and does not have to be used. You would have to be creative in using it because of the quality. It does not have to be used at all. I also added some pictures I liked that could be used. I think I like the "Empty church opening" the best. Fits the theme perfectly.

Target Market(s)

30 years old and older.

Requirements
Must have
• Warmth
Nice to have
• I attached two pictures. One of an empty church and one with a reflection of a stain glass window on the wall. It would be nice to see some offerings using these pictures.
Should not have
• Not too churchy

```html
<!DOCTYPE html>
<html lang="en">
<head>
<meta charset="utf-8">
<title>Neil Harwood – Beyond the Orchard Gate</title>
<link rel="stylesheet" href="https://fonts.googleapis.com/css2?family=Poppins:wght@600;700&family=Raleway:wght@300;400;700&display=swap">
<style>
  :root {
    --backdrop: #e9e5e2;
    --ink-light: #ffffff;
    --ink-soft: #f6f0e6;
    --ink-muted: #b9ab96;
    --shadow-dark: #120c08;
    --wall-brown: #3a2a1c;
    --frame-line: rgba(255, 255, 255, 0.55);
    --portrait-grey: #8d8d90;
  }
  * { box-sizing: border-box; margin: 0; padding: 0; }
  html, body {
    width: 1200px; height: 600px; overflow: hidden;
    background: var(--backdrop);
  }
  .canvas { position: relative; width: 1200px; height: 600px; }

  .panel {
    position: absolute; top: 72px; width: 456px; height: 456px;
    overflow: hidden; color: var(--ink-light);
  }
  .panel--front { left: 118px; }
  .panel--back { left: 627px; }

  .panel__photo {
    position: absolute; inset: 0;
    background:
      linear-gradient(115deg,
        transparent 0%, transparent 38%,
        rgba(90, 47, 192, 0.85) 46%,
        rgba(111, 182, 224, 0.7) 52%,
        rgba(242, 210, 26, 0.9) 58%,
        rgba(201, 138, 42, 0.75) 68%,
        transparent 82%),
      radial-gradient(ellipse at 20% 10%, #6d5a48 0%, var(--wall-brown) 30%, var(--shadow-dark) 75%);
  }
  .panel--back .panel__photo { opacity: 0.75; }
  .panel--back .panel__veil {
    position: absolute; inset: 0;
    background: linear-gradient(180deg, rgba(18,12,8,0.15), rgba(18,12,8,0.45));
  }

  /* Front */
  .title-frame {
    position: absolute; left: 72px; top: 74px; width: 310px; height: 309px;
    border: 1px solid var(--frame-line);
  }
  .front-title {
    position: absolute; left: 0; right: 0; top: 308px; text-align: center;
  }
  .artist-name {
    font-family: "Poppins", sans-serif; font-weight: 600;
    font-size: 37px; line-height: 1; letter-spacing: -0.5px;
  }
  .album-title {
    font-family: "Raleway", sans-serif; font-weight: 700;
    font-size: 9.5px; letter-spacing: 5.4px; margin-top: 5px;
    text-transform: uppercase;
  }

  /* Back */
  .portrait {
    position: absolute; left: 187px; top: 38px; width: 80px; height: 80px;
    border-radius: 50%; background: radial-gradient(circle at 50% 40%, #a9a9ac, var(--portrait-grey));
  }
  .back-title { position: absolute; left: 0; right: 0; top: 128px; text-align: center; }
  .back-title .artist-name { font-size: 25px; }
  .back-title .album-title { font-size: 7px; letter-spacing: 3.6px; margin-top: 3px; }

  .tracklist {
    position: absolute; left: 0; right: 0; top: 186px;
    list-style: none; text-align: center;
    font-family: "Raleway", sans-serif; font-weight: 300;
    font-size: 11.5px; line-height: 16px; color: var(--ink-soft);
  }

  .label {
    position: absolute; top: 376px; left: 152px;
    display: flex; align-items: center; gap: 47px;
    font-family: "Raleway", sans-serif;
  }
  .label__mark {
    width: 36px; height: 36px; border-radius: 50%;
    border: 1.5px solid var(--ink-light); flex: none;
  }
  .label__name { font-weight: 700; font-size: 8px; letter-spacing: 0.2px; text-transform: uppercase; }
  .label__address { font-weight: 400; font-size: 7.5px; color: var(--ink-muted); margin-top: 2px; }

  .credits {
    position: absolute; left: 0; right: 0; top: 421px; text-align: center;
    font-family: "Raleway", sans-serif; font-weight: 400;
    font-size: 7.2px; line-height: 11px; color: var(--ink-soft);
  }
  .credits strong { font-weight: 700; color: var(--ink-light); }
</style>
</head>
<body>
<main class="canvas">

  <section class="panel panel--front" aria-label="Front cover">
    <div class="panel__photo" role="img" aria-label="Dim chapel interior with coloured light from a stained glass window streaming across a plaster wall"></div>
    <div class="title-frame"></div>
    <header class="front-title">
      <h1 class="artist-name">Neil Harwood</h1>
      <p class="album-title">Beyond the Orchard Gate</p>
    </header>
  </section>

  <section class="panel panel--back" aria-label="Back cover">
    <div class="panel__photo" role="img" aria-label="Dim chapel interior with coloured window light on the wall"></div>
    <div class="panel__veil"></div>
    <div class="portrait" role="img" aria-label="Portrait photo of the artist"></div>
    <header class="back-title">
      <h2 class="artist-name">Neil Harwood</h2>
      <p class="album-title">Beyond the Orchard Gate</p>
    </header>
    <ol class="tracklist">
      <li>Morning Letter</li>
      <li>Beyond the Orchard Gate</li>
      <li>Common Neighbors</li>
      <li>The Night the Lanterns Burned</li>
      <li>Risen Light</li>
      <li>Another Hymn at Dusk</li>
      <li>The Quiet Psalm</li>
      <li>Back Along the River</li>
      <li>Mercy on the Hill</li>
      <li>When the Fields Turn Gold</li>
    </ol>
    <div class="label">
      <span class="label__mark"></span>
      <div>
        <p class="label__name">Meadowlark Records</p>
        <p class="label__address">Fairview, OR 97024</p>
      </div>
    </div>
    <p class="credits">
      <strong>Producer</strong> Della Marsh, <strong>Engineered</strong> Peter Kowalczyk, <strong>Promoter</strong> Ray Linden,<br>
      <strong>Recorded at</strong> Meadowlark Studio
    </p>
  </section>

</main>
</body>
</html>
```